BirchLane Hotel
BUSINESS CARDS, LETTERHEAD, ENVELOPES, FAX COVER, EMAIL SIGNATURE, signage, car
BirchLane Hotel - Hospitality Industry
Creative Brief
Simple
DOHYUN KWAK
President & C.E.O
B2 Sora Bldg. 412-5 Mokhwa-dong, Seocho-gu, Seoul, 137-914, Korea
oliver@blhotelgroup.com
www.blhotelgroup.com
BirchLane Pohang: 218-4 Hwajin-dong, Bukgu, Pohang, Korea BirchLane Gunsan: 457 Maeryeong-dong, Gunsan, Korea

```html
<!DOCTYPE html>
<html lang="en">
<head>
<meta charset="utf-8">
<title>BirchLane Hotel Business Cards</title>
<link href="https://fonts.googleapis.com/css2?family=Arimo:wght@400;700&display=swap" rel="stylesheet">
<style>
  :root {
    --backdrop: #5a5a5a;
    --card-green: #6cbd2e;
    --tab-white: #ffffff;
    --ink-dark: #2b2b2b;
    --ink-light: #ffffff;
    --mark-red: #d9412b;
  }
  * { margin: 0; padding: 0; box-sizing: border-box; }
  html, body { width: 1200px; height: 961px; overflow: hidden; }
  body {
    background: var(--backdrop);
    font-family: "Arimo", Arial, sans-serif;
    position: relative;
  }
  .card {
    position: absolute;
    top: 340px;
    width: 483px;
    height: 278px;
    background: var(--card-green);
  }
  .card--front { left: 109px; }
  .card--back { left: 610px; }
  .tab {
    position: absolute;
    left: 151px;
    top: 0;
    width: 182px;
    height: 179px;
    background: var(--tab-white);
    border-radius: 0 0 16px 16px;
  }
  .card--back .tab { height: 187px; }
  .brand {
    position: absolute;
    left: 0;
    right: 0;
    top: 58px;
    display: flex;
    flex-direction: column;
    align-items: center;
    gap: 8px;
  }
  .brand-dot {
    width: 30px;
    height: 30px;
    border-radius: 50%;
    background: var(--mark-red);
  }
  .brand-name {
    font-size: 13px;
    font-weight: 700;
    color: var(--ink-dark);
  }
  .website {
    position: absolute;
    left: 151px;
    width: 182px;
    top: 191px;
    text-align: center;
    font-size: 11px;
    font-weight: 700;
    color: var(--ink-light);
  }
  .person {
    position: absolute;
    left: 0;
    right: 0;
    top: 137px;
    text-align: center;
    color: var(--ink-dark);
  }
  .person-name { font-size: 15px; font-weight: 700; line-height: 19px; }
  .person-title { font-size: 11px; line-height: 15px; }
  .contact {
    position: absolute;
    left: 221px;
    top: 195px;
    font-size: 8px;
    line-height: 13px;
    font-weight: 700;
    color: var(--ink-light);
  }
  .address {
    position: absolute;
    left: 0;
    right: 0;
    top: 240px;
    padding-left: 120px;
    font-size: 8px;
    font-weight: 700;
    color: var(--ink-light);
    text-align: center;
  }
</style>
</head>
<body>
  <section class="card card--front">
    <div class="tab">
      <div class="brand">
        <span class="brand-dot"></span>
        <span class="brand-name">BirchLane Hotel</span>
      </div>
    </div>
    <p class="website">www.blhotelgroup.com</p>
  </section>

  <section class="card card--back">
    <div class="tab">
      <div class="brand">
        <span class="brand-dot"></span>
        <span class="brand-name">BirchLane Hotel</span>
      </div>
      <div class="person">
        <p class="person-name">Seojun Baek</p>
        <p class="person-title">General Manager</p>
      </div>
    </div>
    <div class="contact">
      <p>T 02-555-0174</p>
      <p>F 02-555-0175</p>
      <p>C 010-555-0148</p>
    </div>
    <p class="address">B2 Sora Bldg. 412-5 Mokhwa-dong, Seoul, Korea</p>
  </section>
</body>
</html>
```